WEBSITE REFRESH / REDESIGN- USE OLD WEBSITE TO CONSTRUCT NEW TEMPLATE

The current website was designed years ago, and we is now outdated.

We are looking for an updated design to our old website. We are looking for something that is consumer friendly, shows sophistication and is pleasing to the eye and modern.

Our old website consists of 25 pages. You are not required to design new text other from copying and pasting the current text and images.

The redesign requires the site to be modern, easy to navigate.

The current website is: www.brovelwood.com.au, every page must be included and titled the same as the old one.

The home page requires a large slider, that I can change easily often.

Any new ideas are welcome.

I do have a template that I have purchased, however this isn't required to be used....any new exciting ideas will be considered.

Target Market(s)

existing customers; new customers demonstrating what we are offering to sell

Coding

Font styles to use
Sans Serif

Colors
85cae6
33a6d7
0293ce
86cfc6
33b8a4
add136
fbee3e
fbf289
faa54b

Requirements
Must have
• text and photos from existing site. every page needs to be included in redesign.

```html
<!DOCTYPE html>
<html lang="en">
<head>
<meta charset="utf-8">
<title>Brovelwood Timber – Home</title>
<link href="https://fonts.googleapis.com/css2?family=Montserrat:wght@400;600;700;800&family=Open+Sans:wght@400;600;700&display=swap" rel="stylesheet">
<style>
:root{
  --sky:#85cae6;
  --blue:#33a6d7;
  --deep-blue:#0293ce;
  --mint:#86cfc6;
  --teal:#33b8a4;
  --lime:#add136;
  --yellow:#fbee3e;
  --pale-yellow:#fbf289;
  --orange:#faa54b;
  --navy:#1f3550;
  --ink:#3a4450;
  --muted:#8a939c;
  --line:#e3e6e9;
  --soft:#f3f4f5;
  --footer:#3b4650;
  --white:#ffffff;
}
*{box-sizing:border-box;margin:0;padding:0}
html,body{width:783px;height:1200px;overflow:hidden;background:var(--white)}
body{font-family:"Open Sans",Arial,sans-serif;color:var(--ink);font-size:11px}
.page{width:783px;height:1200px;display:flex;flex-direction:column}

/* header */
.site-header{height:50px;display:flex;align-items:center;justify-content:space-between;padding:0 36px;border-bottom:1px solid var(--line)}
.brand{display:flex;align-items:center;gap:8px;font-family:"Montserrat",sans-serif;font-weight:800;font-size:15px;color:var(--navy);letter-spacing:.5px}
.brand-square{width:14px;height:14px;background:var(--navy)}
.main-nav{display:flex;align-items:center;gap:20px;font-family:"Montserrat",sans-serif;font-size:9px;font-weight:600;color:var(--ink);text-transform:uppercase}
.main-nav .active{color:var(--deep-blue)}
.quote-button{background:var(--lime);color:var(--white);padding:6px 14px;border-radius:2px}

/* hero slider */
.hero{position:relative;height:250px}
.hero-photo{position:absolute;inset:0;background:linear-gradient(120deg,#6b4a33 0%,#a87a55 35%,#c79a72 55%,#8e6a4e 75%,#5a5c60 100%)}
.hero-copy{position:absolute;right:60px;top:34px;width:220px;text-align:left}
.hero-title{font-family:"Montserrat",sans-serif;font-weight:800;font-size:38px;line-height:.95;color:var(--navy);text-transform:uppercase}
.hero-title span{display:block;color:var(--deep-blue)}
.hero-note{font-size:10px;color:var(--white);margin:8px 0 4px;font-style:italic}
.price-badge{display:inline-block;background:var(--yellow);color:var(--navy);font-family:"Montserrat",sans-serif;font-weight:800;font-size:30px;padding:4px 14px}
.price-badge small{font-size:16px;vertical-align:top}
.price-unit{font-size:9px;color:var(--white);margin-top:4px}
.hero-button{display:inline-block;margin-top:12px;background:var(--deep-blue);color:var(--white);font-size:9px;font-weight:700;padding:6px 18px;border-radius:12px;text-transform:uppercase}

/* service band */
.service-band{height:120px;background:linear-gradient(180deg,var(--mint),var(--teal));display:flex;gap:10px;padding:18px 50px}
.service-card{flex:1;display:flex;flex-direction:column;align-items:center;justify-content:center;gap:10px;color:var(--white);font-family:"Montserrat",sans-serif;font-size:9px;font-weight:600;text-transform:uppercase;text-align:center}
.service-card.featured{background:rgba(20,100,95,.35);border:1px solid rgba(255,255,255,.5);padding:10px;line-height:1.5;text-transform:none;font-weight:600;font-size:10px}

/* products */
.products{height:220px;padding:16px 60px 0;text-align:center}
.products-intro{font-size:9px;color:var(--muted);margin-bottom:12px}
.product-row{display:flex;gap:12px}
.product-card{flex:1;height:150px;display:flex;flex-direction:column}
.product-photo{flex:1}
.product-photo.one{background:linear-gradient(160deg,#b89874,#7d6a57)}
.product-photo.two{background:linear-gradient(160deg,#c7a482,#8a6b4d)}
.product-photo.three{background:linear-gradient(160deg,#a98663,#6f5845)}
.product-photo.four{background:linear-gradient(160deg,#d29b76,#9a5f3d)}
.product-caption{height:26px;background:var(--footer);color:var(--white);font-size:9px;font-weight:600;display:flex;align-items:center;padding:0 10px}
.product-caption.current{background:var(--deep-blue)}
.slider-dots{display:flex;justify-content:center;gap:5px;margin-top:10px}
.slider-dots i{width:6px;height:6px;border-radius:50%;background:var(--line)}
.slider-dots i.on{background:var(--deep-blue)}

/* about */
.about{height:230px;display:flex;background:var(--soft)}
.about-photo{width:390px;background:linear-gradient(135deg,#e7c79d 0%,#b98752 45%,#7a5533 100%)}
.about-copy{flex:1;padding:30px 40px 0 34px}
.about-title{font-family:"Montserrat",sans-serif;font-weight:700;font-size:17px;line-height:1.3;color:var(--navy)}
.about-lead{font-size:9px;color:var(--teal);margin:6px 0 10px}
.about-text{font-size:9px;line-height:1.6;color:var(--muted)}
.about-button{display:inline-block;margin-top:14px;background:var(--blue);color:var(--white);font-size:9px;font-weight:700;padding:6px 18px;border-radius:12px;text-transform:uppercase}

/* contact */
.contact{height:300px;padding:30px 150px 0;text-align:center}
.contact-title{font-family:"Montserrat",sans-serif;font-weight:700;font-size:17px;color:var(--navy)}
.contact-sub{font-size:9px;color:var(--teal);margin-top:4px}
.contact-points{display:flex;justify-content:space-between;margin:22px 20px 18px}
.contact-point{width:130px;display:flex;flex-direction:column;align-items:center;gap:6px;font-size:8px;color:var(--muted);line-height:1.5}
.contact-point b{color:var(--ink);font-size:9px}
.icon-ring{width:30px;height:30px;border-radius:50%;border:1.5px solid var(--teal);display:flex;align-items:center;justify-content:center}
.form-label{font-size:9px;font-weight:700;color:var(--ink);margin-bottom:8px;text-transform:uppercase}
.field-row{display:flex;gap:8px;margin-bottom:8px}
.field{flex:1;height:22px;border:1px solid var(--line);font-size:8px;color:var(--muted);text-align:left;padding:5px 8px}
.field.message{height:44px}
.send{display:flex;justify-content:flex-end;margin-top:6px}
.send-dot{width:16px;height:16px;border-radius:50%;background:var(--lime);display:flex;align-items:center;justify-content:center}

/* footer */
.site-footer{height:30px;background:var(--footer);color:#c9d0d6;font-size:8px;display:flex;align-items:center;justify-content:space-between;padding:0 36px}
.footer-links{display:flex;gap:16px}
</style>
</head>
<body>
<div class="page">

  <header class="site-header">
    <div class="brand"><span class="brand-square"></span>BROVELWOOD</div>
    <nav class="main-nav">
      <span class="active">Home</span>
      <span>About</span>
      <span>Products</span>
      <span>Services</span>
      <span>Gallery</span>
      <span class="quote-button">Get a Quote</span>
    </nav>
  </header>

  <section class="hero">
    <div class="hero-photo" role="img" aria-label="Stacked cypress timber sleepers in a timber yard"></div>
    <div class="hero-copy">
      <h1 class="hero-title">Cypress<span>Sleepers</span></h1>
      <p class="hero-note">from only</p>
      <div class="price-badge"><small>$</small>25.00</div>
      <p class="price-unit">per sleeper, while stocks last</p>
      <span class="hero-button">Shop Now</span>
    </div>
  </section>

  <section class="service-band">
    <div class="service-card featured">Timber fencing, decking and flooring supplies for every project</div>
    <div class="service-card">
      <svg width="26" height="26" viewBox="0 0 26 26" fill="none" stroke="#fff" stroke-width="2"><path d="M4 22 L18 8 M16 4 L22 10 M4 22 L8 22 L8 18"/></svg>
      Fencing
    </div>
    <div class="service-card">
      <svg width="26" height="26" viewBox="0 0 26 26" fill="none" stroke="#fff" stroke-width="2"><rect x="4" y="6" width="18" height="4"/><rect x="4" y="12" width="18" height="4"/><rect x="4" y="18" width="18" height="4"/></svg>
      Decking
    </div>
    <div class="service-card">
      <svg width="26" height="26" viewBox="0 0 26 26" fill="none" stroke="#fff" stroke-width="2"><path d="M4 20 L22 20 M6 20 L6 8 L20 8 L20 20 M10 8 L10 20 M16 8 L16 20"/></svg>
      Flooring
    </div>
  </section>

  <section class="products">
    <p class="products-intro">Browse our range of quality timber products available for delivery across Melbourne</p>
    <div class="product-row">
      <div class="product-card"><div class="product-photo one" role="img" aria-label="Bundle of treated pine sleepers"></div><div class="product-caption">Treated Pine</div></div>
      <div class="product-card"><div class="product-photo two" role="img" aria-label="Stack of hardwood sleepers"></div><div class="product-caption current">Hardwood Sleepers</div></div>
      <div class="product-card"><div class="product-photo three" role="img" aria-label="Pile of fencing palings"></div><div class="product-caption">Fence Palings</div></div>
      <div class="product-card"><div class="product-photo four" role="img" aria-label="Merbau decking boards"></div><div class="product-caption">Merbau Decking</div></div>
    </div>
    <div class="slider-dots"><i class="on"></i><i></i><i></i></div>
  </section>

  <section class="about">
    <div class="about-photo" role="img" aria-label="Close-up of cut timber block ends"></div>
    <div class="about-copy">
      <h2 class="about-title">We are a Melbourne timber fencing, decking and flooring supplier</h2>
      <p class="about-lead">Family owned and operated for over thirty years</p>
      <p class="about-text">We supply builders, landscapers and home owners with quality timber at fair prices. Our friendly team can help you choose the right product, cut it to size and deliver it straight to your site.</p>
      <span class="about-button">Read More</span>
    </div>
  </section>

  <section class="contact">
    <h2 class="contact-title">Have Question? Contact Us</h2>
    <p class="contact-sub">Our team is happy to help with any enquiry</p>
    <div class="contact-points">
      <div class="contact-point">
        <span class="icon-ring"><svg width="14" height="14" viewBox="0 0 14 14" fill="none" stroke="#33b8a4" stroke-width="1.5"><path d="M7 13 C3 8 2 6 2 5 A5 5 0 0 1 12 5 C12 6 11 8 7 13Z"/><circle cx="7" cy="5" r="1.6"/></svg></span>
        <b>Our Location</b>12 Mill Road, Dandenong VIC
      </div>
      <div class="contact-point">
        <span class="icon-ring"><svg width="14" height="14" viewBox="0 0 14 14" fill="none" stroke="#33b8a4" stroke-width="1.5"><path d="M3 2 L5 2 L6 5 L4.5 6 A7 7 0 0 0 8 9.5 L9 8 L12 9 L12 11 C12 12 11 12.5 10 12.5 A9 9 0 0 1 1.5 4 C1.5 3 2 2 3 2Z"/></svg></span>
        <b>Opening Hours</b>Mon–Fri 7am – 4pm<br>Phone 03 9000 1234
      </div>
      <div class="contact-point">
        <span class="icon-ring"><svg width="14" height="14" viewBox="0 0 14 14" fill="none" stroke="#33b8a4" stroke-width="1.5"><rect x="1.5" y="3" width="11" height="8"/><path d="M1.5 3 L7 8 L12.5 3"/></svg></span>
        <b>Email Us</b>sales@brovelwood.com.au
      </div>
    </div>
    <p class="form-label">Send a Message</p>
    <div class="field-row"><div class="field">Your Name</div><div class="field">Your Email</div><div class="field">Phone</div></div>
    <div class="field message">Your Message</div>
    <div class="send"><span class="send-dot"><svg width="8" height="8" viewBox="0 0 8 8" fill="none" stroke="#fff" stroke-width="1.5"><path d="M2 1 L6 4 L2 7"/></svg></span></div>
  </section>

  <footer class="site-footer">
    <div class="footer-links"><span>© Brovelwood Timber</span><span>Privacy Policy</span><span>Terms</span></div>
    <span>www.brovelwood.com.au</span>
  </footer>

</div>
</body>
</html>
```